Branded Resources for OVARTe--Word, PPT, Newsletter Templates

Hi,
I hope you are well. I am hoping to get some pricing on branding a Word and PPT template and a Newsletter template. I've uploaded the original files for quick reference.

I was hoping for a full-color version and a black/grayscale version of the word and PPT template. Full color for the newsletter.

Thanks in advance for your quote and expected timeline for this project.

Thanks,
Belosa
Updates

Thank you for your submission and patience. I had a family emergency, and just getting back online. I will review the submissions. Thank you. Belosa

Industry/Entity Type

management consulting. Here's my website: https://ovarte-example.com/

Requirements
Must have
• The Word, PPT and Newsletter templates should reflect the logo assets listed below. Open to complementary colors that complement red/orange/golds
Nice to have
• Vibrancy, diversity, community

```html
<!DOCTYPE html>
<html lang="en">
<head>
<meta charset="utf-8">
<title>OVARTe Letterhead</title>
<link href="https://fonts.googleapis.com/css2?family=Montserrat:wght@400;700&family=Roboto+Condensed:wght@700&display=swap" rel="stylesheet">
<style>
:root{
  --stage:#878887;
  --paper:#ffffff;
  --ink:#2b2b2b;
  --text:#333333;
  --maroon:#77231f;
  --orange:#dc8b2a;
  --black:#000000;
}
*{margin:0;padding:0;box-sizing:border-box}
html,body{width:1200px;height:1200px;overflow:hidden;background:var(--stage)}
.letterhead{position:absolute;left:276px;top:181px;width:647px;height:837px;background:var(--paper);overflow:hidden;font-family:"Montserrat",sans-serif;color:var(--text)}
.swoosh{position:absolute;left:0;top:0;width:647px;height:837px}
.brand{position:absolute;left:509px;top:30px;width:100px;text-align:center}
.brand-dot{display:block;margin:0 auto;width:92px;height:92px;border-radius:50%;background:var(--ink)}
.brand-name{display:block;margin-top:6px;font-family:"Montserrat",sans-serif;font-weight:700;font-size:16px;letter-spacing:1px;color:var(--ink)}
.title{position:absolute;left:59px;top:156px;font-weight:700;font-size:17.5px;color:var(--text)}
.body p{font-size:11.7px;line-height:17.7px;font-weight:400;color:var(--text)}
.intro{position:absolute;left:60px;top:195px;width:540px}
.intro p+p{margin-top:14px}
.col{position:absolute;top:441px}
.col p+p{margin-top:14px}
.col-left{left:60px;width:256px}
.col-right{left:339px;width:248px}
.contacts{position:absolute;left:60px;top:801px;width:560px;height:14px;font-family:"Roboto Condensed",sans-serif;font-weight:700;font-size:8.6px;color:#222}
.contact{position:absolute;top:0;display:flex;align-items:center;gap:6px;white-space:nowrap}
.contact svg{width:12px;height:12px}
.band{position:absolute;left:0;bottom:0;width:647px;height:16px;background:var(--maroon)}
</style>
</head>
<body>
<main class="letterhead">
  <svg class="swoosh" viewBox="0 0 1042 1348" preserveAspectRatio="none" aria-hidden="true">
    <path d="M0,0 H525 C300,40 90,170 0,368 Z" fill="var(--maroon)"/>
    <path d="M0,0 H385 C250,55 130,160 40,300 L0,355 Z" fill="var(--black)"/>
    <path d="M0,175 C80,112 170,62 258,25 C150,95 55,210 0,358 Z" fill="var(--orange)"/>
  </svg>

  <div class="brand">
    <span class="brand-dot"></span>
    <span class="brand-name">OVARTe</span>
  </div>

  <h1 class="title">Lorem ipsum dolor sit amet</h1>

  <section class="body">
    <div class="intro">
      <p>Lorem ipsum dolor sit amet, consectetur adipiscing elit. Duis auctor sem vel metus interdum porta. Duis consequat bibendum felis eget cursus. Nulla eget purus vehicula ipsum finibus egestas. Nullam ligula ipsum, mollis sed gravida vitae, maximus eu dolor. Morbi luctus sem a congue consectetur.</p>
      <p>Orci varius natoque penatibus et magnis dis parturient montes, nascetur ridiculus mus. Vestibulum congue eros auctor, ullamcorper libero blandit, tempor tellus. Proin vitae tellus et nunc fringilla lacinia. Sed augue erat, facilisis laoreet velit a, convallis mattis nunc. Nunc sagittis ligula vitae sollicitudin sollicitudin. Orci varius natoque penatibus et magnis dis parturient montes, nascetur ridiculus mus. Vestibulum congue eros auctor, ullamcorper libero blandit, tempor tellus. Proin vitae tellus et nunc fringilla lacinia. Sed augue erat, facilisis laoreet velit a, convallis mattis nunc. Nunc sagittis ligula vitae sollicitudin sollicitudin.</p>
    </div>
    <div class="col col-left">
      <p>Lorem ipsum dolor sit amet, consectetur adipiscing elit. Duis auctor sem vel metus interdum porta. Duis consequat bibendum felis eget cursus. Nulla eget purus vehicula ipsum finibus egestas. Nullam ligula ipsum, mollis sed gravida vitae, maximus eu dolor. Morbi luctus sem a congue consectetur.</p>
      <p>Orci varius natoque penatibus et magnis dis parturient montes, nascetur ridiculus mus. Vestibulum congue eros auctor, ullamcorper libero blandit, tempor tellus. Proin vitae tellus et nunc fringilla lacinia. Sed augue erat, facilisis laoreet velit a, convallis mattis nunc. Nunc sagittis ligula vitae sollicitudin sollicitudin. Orci varius natoque penatibus et magnis dis parturient montes, nascetur ridiculus mus.</p>
    </div>
    <div class="col col-right">
      <p>Vestibulum congue eros auctor, ullamcorper libero blandit, tempor tellus. Proin vitae tellus et nunc fringilla lacinia. Sed augue erat, facilisis laoreet velit a, convallis mattis nunc. Nunc sagittis ligula vitae sollicitudin sollicitudin.</p>
      <p>Nulla facilisi. Nulla quis odio vitae purus aliquam fermentum ut nec diam. Fusce sed velit ultrices, aliquam augue ut, sollicitudin orci. Orci varius natoque penatibus et magnis dis parturient montes, nascetur ridiculus mus. Vestibulum congue eros auctor, ullamcorper libero blandit, tempor tellus. Proin vitae tellus et nunc fringilla lacinia. Sed augue erat, facilisis laoreet velit a, convallis mattis nunc. Nunc sagittis ligula vitae sollicitudin sollicitudin.</p>
    </div>
  </section>

  <footer class="contacts">
    <div class="contact" style="left:0">
      <svg viewBox="0 0 12 12"><circle cx="6" cy="6" r="6" fill="var(--maroon)"/><rect x="4" y="2.5" width="4" height="7" rx="0.8" fill="#fff"/><rect x="4.7" y="3.3" width="2.6" height="4.6" fill="var(--maroon)"/></svg>
      <span>0123 456 790</span>
    </div>
    <div class="contact" style="left:102px">
      <svg viewBox="0 0 12 12"><circle cx="6" cy="6" r="6" fill="var(--maroon)"/><rect x="3" y="4" width="6" height="4.2" fill="#fff"/><path d="M3,4 L6,6.4 L9,4" stroke="var(--maroon)" stroke-width="0.7" fill="none"/></svg>
      <span>info@yourwebnamae.com</span>
    </div>
    <div class="contact" style="left:255px">
      <svg viewBox="0 0 12 12"><circle cx="6" cy="6" r="6" fill="var(--maroon)"/><circle cx="6" cy="6" r="3.3" fill="none" stroke="#fff" stroke-width="0.7"/><path d="M2.7,6 H9.3 M6,2.7 V9.3" stroke="#fff" stroke-width="0.6"/><ellipse cx="6" cy="6" rx="1.5" ry="3.3" fill="none" stroke="#fff" stroke-width="0.6"/></svg>
      <span>www.yourwebnamae.com</span>
    </div>
    <div class="contact" style="left:400px">
      <svg viewBox="0 0 12 12"><path d="M6,0.5 C3,0.5 1.5,2.6 1.5,4.8 C1.5,7.8 6,11.5 6,11.5 C6,11.5 10.5,7.8 10.5,4.8 C10.5,2.6 9,0.5 6,0.5 Z" fill="var(--maroon)"/><circle cx="6" cy="4.8" r="1.7" fill="#fff"/></svg>
      <span>1235456, your location.23923923</span>
    </div>
  </footer>

  <div class="band"></div>
</main>
</body>
</html>
```